Harborview Behavioral and Community Services

Intellectual Developmental Disabilities, Group Homes, Residential Homes and Substance Abuse Residential facilities

Target Market(s)

Adults 18-59 male and female autism, developmental disabilities and mental health

Industry/Entity Type

Intellectual Development Disabilities, Autism, Applied Behavioral Analysis, Mental Health, Substance Abuse

Coding

Coded - Design and coding required

Number of Pages Required

5+ page

Font styles to use
Serif

Colors
0054AA
0677BA
7BADD7
CADEEF
E8F1F8

Requirements
Should not have
• Not specified

```html
<!DOCTYPE html>
<html lang="en">
<head>
<meta charset="utf-8">
<title>Harborview Behavioral and Community Services</title>
<link href="https://fonts.googleapis.com/css2?family=Lora:wght@400;500;600;700&display=swap" rel="stylesheet">
<style>
:root{
  --navy:#0054AA;
  --blue:#0677BA;
  --sky:#7BADD7;
  --pale:#CADEEF;
  --mist:#E8F1F8;
  --ink:#1c1c1c;
  --muted:#666;
  --white:#fff;
}
*{box-sizing:border-box;margin:0;padding:0}
html,body{width:1200px;height:3710px;overflow:hidden}
body{position:relative;font-family:'Lora',serif;color:var(--ink);background:var(--white)}
.abs{position:absolute}
.btn{position:absolute;display:flex;align-items:center;justify-content:center;border-radius:6px;font-size:14px;font-weight:600;color:var(--white);background:var(--blue)}
.btn-outline{background:transparent;border:2px solid var(--white)}
.photo{position:absolute}
.hero{position:absolute;left:0;top:0;width:1200px;height:746px}
.hero-shade{position:absolute;inset:0;background:linear-gradient(90deg,rgba(20,25,30,.55),rgba(20,25,30,.1) 65%)}
.nav-line{position:absolute;left:0;top:88px;width:1200px;height:1px;background:rgba(255,255,255,.25)}
.logo{font-weight:700;font-size:35px;line-height:44px;color:var(--white)}
.nav{position:absolute;left:361px;top:35px;display:flex;gap:28px;font-size:14px;color:var(--white)}
.badge{left:89px;top:202px;width:152px;height:35px;border-radius:6px;background:var(--pale);color:var(--ink);font-size:14px;font-weight:500;display:flex;align-items:center;justify-content:center}
.hero-title{left:89px;top:250px;font-size:56px;line-height:58px;font-weight:700;color:var(--white)}
.hero-text{left:92px;top:437px;width:540px;font-size:13.5px;line-height:22px;color:var(--white)}
.scroll{left:578px;top:660px;width:44px;height:68px;border:2px solid var(--white);border-radius:22px}
h2{font-weight:700;font-size:36px;line-height:44px;color:var(--ink)}
.body-text{font-size:13px;line-height:22px;color:var(--muted)}
.card{position:absolute;border-radius:10px;overflow:hidden}
.card-label{position:absolute;left:0;right:0;bottom:12px;text-align:center;color:var(--white);font-weight:600;font-size:16px;line-height:22px}
.story{left:89px;top:1925px;width:1022px;height:420px;border-radius:25px;background:var(--sky)}
.news{position:absolute;top:2943px;width:258px;height:279px;border-radius:10px;background:var(--mist);overflow:hidden}
.news-img{height:180px}
.date{position:absolute;left:20px;top:165px;padding:6px 24px;border-radius:16px;background:var(--pale);font-size:14px;font-weight:500}
.news h3{position:absolute;left:17px;top:218px;font-size:16px;font-weight:600;line-height:22px}
.footer{position:absolute;left:0;top:3325px;width:1200px;height:385px;background:var(--blue);color:var(--white)}
.footer h4{font-size:25px;font-weight:600;margin-bottom:14px}
.footer ul{list-style:none;font-size:13px;line-height:24px}
.contact-row{display:flex;gap:10px;font-size:13px;line-height:16px;margin-bottom:14px}
</style>
</head>
<body>

<header class="hero">
  <div class="photo" role="img" aria-label="Photo of a smiling woman in a wheelchair with a girl standing behind her in a park" style="inset:0;background:linear-gradient(90deg,#3f433f 0%,#5d5c57 40%,#8f8a82 65%,#7a736c 100%)"></div>
  <div class="hero-shade"></div>
  <div class="abs logo" style="left:87px;top:20px">Harborview</div>
  <nav class="nav"><span>Home</span><span>About Us</span><span>Our Services</span><span>Find Support</span><span>Success Stories</span><span>Careers</span></nav>
  <div class="btn" style="left:972px;top:22px;width:138px;height:44px">Contact Us</div>
  <div class="nav-line"></div>
  <div class="abs badge">Welcome To</div>
  <h1 class="abs hero-title">Empowering<br>Lives Transforming<br>Communities</h1>
  <p class="abs hero-text">We are committed to helping individuals with intellectual disabilities, autism, and mental health challenges lead fulfilling and independent lives.</p>
  <div class="btn" style="left:89px;top:500px;width:143px;height:46px">Apply Now</div>
  <div class="btn btn-outline" style="left:242px;top:500px;width:160px;height:46px">Donate Today</div>
  <div class="abs scroll"><svg width="40" height="64" viewBox="0 0 40 64"><path d="M20 22v20M13 35l7 7 7-7" stroke="#fff" stroke-width="2" fill="none"/></svg></div>
</header>

<section class="about">
  <div class="photo" role="img" aria-label="Photo of a caregiver in blue scrubs pushing an older woman in a wheelchair" style="left:118px;top:855px;width:364px;height:415px;border-radius:22px;background:linear-gradient(160deg,#c9ccce,#8d9094 60%,#6d7073)"></div>
  <h2 class="abs" style="left:545px;top:880px">A Community<br>That Feels Like Home</h2>
  <div class="abs body-text" style="left:545px;top:981px;width:535px">
    <p>For years, we have been a trusted provider of developmental and behavioral health services offering support that goes beyond care it's about transformation We believe that every individual deserves respect dignity and the right to thrive in their community. Our expert team is dedicated to providing personalized programs that address intellectual disabilities autism spectrum disorders and behavioral health needs.</p>
    <p style="margin-top:14px">Whether it's helping someone develop daily living skills, find meaningful employment, or access critical mental health support, we stand by our commitment to empower, educate, and uplift.</p>
  </div>
  <div class="btn" style="left:545px;top:1215px;width:218px;height:45px">Learn More About Us</div>
</section>

<section class="services">
  <h2 class="abs" style="left:0;width:1200px;top:1362px;text-align:center">Our Services</h2>
  <div class="card" style="left:94px;top:1432px;width:242px;height:258px">
    <div class="photo" role="img" aria-label="Photo of a support worker helping a woman in a wheelchair at a desk" style="inset:0;background:linear-gradient(180deg,#cfd1cf,#7c7a78 55%,#2f2d2c)"></div>
    <div class="card-label">Developmental<br>Disabilities</div></div>
  <div class="card" style="left:350px;top:1432px;width:242px;height:258px">
    <div class="photo" role="img" aria-label="Photo of a man in glasses writing on a whiteboard" style="inset:0;background:linear-gradient(180deg,#e2e0dc,#9a837a 55%,#3a2a26)"></div>
    <div class="card-label">Applied Behavioral<br>Analysis</div></div>
  <div class="card" style="left:607px;top:1432px;width:242px;height:258px">
    <div class="photo" role="img" aria-label="Photo of a therapist taking notes with a distressed client" style="inset:0;background:linear-gradient(180deg,#dcdcd8,#8c8a86 55%,#2c2b2a)"></div>
    <div class="card-label">Behavioral<br>Therapy</div></div>
  <div class="card" style="left:863px;top:1432px;width:242px;height:258px">
    <div class="photo" role="img" aria-label="Photo of a thoughtful young man in a green sweater" style="inset:0;background:linear-gradient(180deg,#d56a52,#b59a86 40%,#6f8a82 70%,#2d3331)"></div>
    <div class="card-label">Substance Abuse<br>Recovery</div></div>
  <div class="btn" style="left:500px;top:1721px;width:201px;height:45px">Explore All Services</div>
</section>

<section class="abs story">
  <h2 class="abs" style="left:46px;top:55px;color:var(--white)">Mia's Path to<br>Independence</h2>
  <p class="abs body-text" style="left:49px;top:154px;width:445px;color:var(--white)">Mia was diagnosed with autism at an early age, &amp; her family struggled to find the right support. Through our specialized programs, she received personalized therapy, life skills training, and social development support. Today, Mia confidently navigates her daily life, attends college, and has built meaningful friendships. Her journey is proof that with the right guidance and care, independence is possible.</p>
  <div class="btn btn-outline" style="left:49px;top:328px;width:186px;height:47px">Read More Stories</div>
</section>
<div class="photo" role="img" aria-label="Photo of a man kneeling and holding hands with a young woman in a wheelchair" style="left:617px;top:1863px;width:441px;height:427px;border-radius:20px;background:linear-gradient(135deg,#cdb16a,#d9c489 35%,#e8e4dc 60%,#b7b2aa)"></div>

<section class="join">
  <div class="photo" role="img" aria-label="Photo of a smiling grey-haired woman in a white shirt seated in a navy armchair" style="left:140px;top:2415px;width:375px;height:375px;border-radius:40px;background:radial-gradient(ellipse at 60% 45%,#f1ece6 0%,#c8c2bb 40%,#2b3c6e 70%,#ffffff 100%)"></div>
  <h2 class="abs" style="left:562px;top:2505px">Join Us<br>In Making a Difference</h2>
  <p class="abs body-text" style="left:564px;top:2598px;width:495px">Every individual deserves the chance to reach their full potential, and you can be a part of that change. Whether you choose to join our dedicated team, volunteer your time, or donate, your support plays a crucial role in shaping lives and strengthening communities.</p>
  <div class="btn" style="left:564px;top:2705px;width:144px;height:45px">Apply Now</div>
</section>

<section class="news-section">
  <h2 class="abs" style="left:0;width:1200px;top:2872px;text-align:center">Latest News &amp; Events</h2>
  <article class="news" style="left:191px">
    <div class="news-img" role="img" aria-label="Photo of two men reviewing work at a laptop" style="background:linear-gradient(160deg,#d6d4d0,#6c4c74 55%,#8c6a5c)"></div>
    <span class="date">28 July 2023</span><h3>Heading Some Blog Goes<br>Here</h3></article>
  <article class="news" style="left:471px">
    <div class="news-img" role="img" aria-label="Photo of a mother and child playing with blocks" style="background:linear-gradient(160deg,#e4ddd2,#b49a84 55%,#7c9ab8)"></div>
    <span class="date">28 July 2023</span><h3>Heading Some Blog Goes<br>Here</h3></article>
  <article class="news" style="left:750px">
    <div class="news-img" role="img" aria-label="Photo of a child in a wheelchair outdoors with bubbles" style="background:linear-gradient(160deg,#9fb478,#c7cfae 45%,#5a5c5e)"></div>
    <span class="date">28 July 2023</span><h3>Heading Some Blog Goes<br>Here</h3></article>
</section>

<footer class="footer">
  <div class="abs logo" style="left:89px;top:148px">Harborview</div>
  <div class="abs" style="left:365px;top:50px"><h4>Quick links</h4>
    <ul><li>Home</li><li>About Us</li><li>Our Services</li><li>Find Support</li><li>Success Stories</li><li>Careers</li><li>Contact</li></ul></div>
  <div class="abs" style="left:613px;top:50px"><h4>Contact info</h4>
    <div class="contact-row"><svg width="12" height="12" viewBox="0 0 12 12"><rect x="0" y="2" width="12" height="8" fill="#fff"/><path d="M0 2l6 4 6-4" stroke="#0677BA" fill="none"/></svg><span>Email:<br>Info@example.com</span></div>
    <div class="contact-row"><svg width="12" height="12" viewBox="0 0 12 12"><path d="M2 1l3 0 1 3-2 1a7 7 0 0 0 3 3l1-2 3 1 0 3c-6 0-9-3-9-9z" fill="#fff"/></svg><span>Phone:<br>(123) 456 789</span></div>
    <div class="contact-row"><svg width="12" height="14" viewBox="0 0 12 14"><path d="M6 0a5 5 0 0 1 5 5c0 4-5 9-5 9S1 9 1 5a5 5 0 0 1 5-5z" fill="#fff"/><circle cx="6" cy="5" r="2" fill="#0677BA"/></svg><span>Location:<br>Addresssomegoeshere</span></div></div>
  <div class="abs" style="left:897px;top:50px;width:215px"><h4>Newsletter</h4>
    <p style="font-size:12px;line-height:16px">Subscribe to our email address to get the latest news.</p>
    <div style="margin-top:18px;height:46px;border-radius:6px;background:var(--navy);display:flex;align-items:center;justify-content:space-between;padding:0 16px;font-size:11.5px">
      <span>&#9993; Enter Your Email...</span>
      <svg width="14" height="14" viewBox="0 0 14 14"><path d="M0 6l14-6-5 14-2-6z" fill="#fff"/></svg></div></div>
  <div class="abs" style="left:89px;top:327px;width:1022px;height:1px;background:rgba(255,255,255,.3)"></div>
  <p class="abs" style="left:0;width:1200px;top:350px;text-align:center;font-size:13px">©2025 Copyright | All Rights Reserved</p>
  <div class="abs" style="left:1132px;top:253px;width:40px;height:40px;border-radius:50%;background:var(--sky);display:flex;align-items:center;justify-content:center">
    <svg width="12" height="8" viewBox="0 0 12 8"><path d="M2 6l4-4 4 4" stroke="#fff" stroke-width="2" fill="none"/></svg></div>
</footer>

</body>
</html>
```